A Brochure to sell LED Downlights to clients

I am starting a campaign on google for LED down lights the link to the landing page can be found at brimfield.com.au/led .

When the client send a contact request i want to be able to send back a brochure of a picture of each light (Approx 6 - 8 types) and have a few sentences on each light and price brake down.

'Parvane Oslira 9w LED'

**Information**

1-10 lights $49
11-20 lights $45
21 - 40 lights $42
40 and over $40

EACH LIGHT:

Hi,

This is very good.

I
But,

Each light will have its own price.

Can i get it made like this;

Picture - Spec - Pricing in a table style please? - i like the layout it just need to suit the tables under:

picture - Brand - Price 1-10
Model - Price 11-20
Watts - Price 21-21
lumen - price 30- 40
Warranty = price 40+

Model - Price 11-20
Watts - Price 21-21
lumen - price 30- 40
Warranty = price 40+

Model - Price 11-20
Watts - Price 21-21
lumen - price 30- 40
Warranty = price 40+

and so on....

I want it to be on Microsoft Word so i can easily chop and edit the prices and images also. (So i can print to PDF)

For more information see my website to seek inspiration. I have a zip file of my logo for actual creation and should be also to source pictures of the lights when finalising the design.

brimfield.com.au

Thanks

Added 2 x additional Dimmers please see zip file, same layout/pricing as the downlights

Target Market(s)

Homeowners/commercial business owners

Industry/Entity Type

Electric Company

Font styles to use
Sans Serif

Colors
86cfc6
ffffff
000000

Requirements
Must have
• Professional looking, Colours to the theme of my logo/website
Nice to have
• An awesome design that sells it's self!!!!!!!
• My Logo font is 'Radikil" it would be nice to follow that theme if it doesn't look good i am open to have a nice legible font for the copy.
Should not have
• Cheesy light globes or images

```html
<!DOCTYPE html>
<html lang="en">
<head>
<meta charset="utf-8">
<title>Brimfield Electrical – LED Downlights Brochure</title>
<link href="https://fonts.googleapis.com/css2?family=Quicksand:wght@500;700&family=Didact+Gothic&display=swap" rel="stylesheet">
<style>
:root{
  --teal:#86cfc6;
  --teal-band:#5f9c98;
  --black:#000000;
  --white:#ffffff;
  --ink:#1a1a1a;
  --rule:#c9c9c9;
}
*{box-sizing:border-box;margin:0;padding:0}
html,body{width:1200px;height:1141px;overflow:hidden;background:var(--white)}
body{position:relative;font-family:"Didact Gothic",sans-serif;color:var(--white)}
.page{position:absolute;width:328px;height:463px;overflow:hidden;box-shadow:0 1px 4px rgba(0,0,0,.25)}
.p1{left:68px;top:67px}.p2{left:436px;top:67px}.p3{left:804px;top:67px}
.p4{left:68px;top:601px}.p5{left:436px;top:601px}.p6{left:804px;top:601px}

/* cover */
.cover{background:var(--white)}
.cover-photo{position:absolute;left:0;top:0;width:328px;height:363px;background:linear-gradient(180deg,#6fb2ab 0%,#5fa39c 55%,#4e8f88 100%)}
.cover-logo{position:absolute;left:169px;top:47px;width:159px;height:88px;background:var(--black);text-align:center;padding-top:30px}
.cover-logo .brand-name{font-size:25px}
.cover-logo .brand-sub{font-size:8px}
.cover-product{position:absolute;left:52px;top:318px;width:120px;height:140px;border-radius:50% 50% 40% 40%;background:radial-gradient(circle at 55% 35%,#f4f4f4 0%,#d9d9d9 55%,#bdbdbd 100%)}
.cover-title{position:absolute;left:178px;top:402px;font-family:"Quicksand",sans-serif;font-weight:700;font-size:17px;color:var(--ink)}

/* brand */
.brand-name{font-family:"Quicksand",sans-serif;font-weight:500;color:var(--teal);font-size:19px;line-height:1;letter-spacing:.3px}
.brand-sub{font-family:"Quicksand",sans-serif;font-weight:500;color:var(--white);font-size:6.5px;letter-spacing:1.6px;margin-top:2px}

/* product sheet */
.sheet-header{position:absolute;left:0;top:0;width:328px;height:69px;background:var(--black);text-align:center;padding-top:28px}
.sheet-photo{position:absolute;left:0;top:69px;width:328px;height:339px}
.sheet-photo::after{content:"";position:absolute;inset:0;background:rgba(20,22,26,.45)}
.photo-a{background:linear-gradient(160deg,#5d6066,#3b3e44 50%,#2a2c31)}
.photo-b{background:linear-gradient(160deg,#4a4846,#5a4a3e 55%,#3a3430)}
.photo-c{background:linear-gradient(160deg,#3e3b45,#4a2f33 60%,#2b2326)}
.photo-d{background:linear-gradient(160deg,#55606b,#3d4753 55%,#2b323b)}
.photo-e{background:linear-gradient(160deg,#4b4b4d,#3a3836 55%,#28272a)}
.product-shot{position:absolute;left:200px;top:98px;width:106px;height:100px;border-radius:50%;background:radial-gradient(circle at 50% 45%,#fbfbfb 0%,#e2e2e2 45%,#a8a8a8 75%,rgba(160,160,160,0) 100%)}
.sheet-title{position:absolute;left:20px;top:96px;font-family:"Quicksand",sans-serif;font-weight:700;font-size:15px}
.title-rule{position:absolute;left:20px;top:118px;width:285px;height:1px;background:rgba(255,255,255,.7)}
.sheet-body{position:absolute;left:20px;top:126px;width:230px}
.intro{width:180px;font-size:8.4px;line-height:12.2px;margin-bottom:8px;white-space:nowrap}
.sec-head{font-style:italic;font-size:8.4px;line-height:11px;margin-top:7px}
.intro + .sec-head{margin-top:0}
.bullets{list-style:none;font-size:6.8px;line-height:10.4px;white-space:nowrap}
.bullets li::before{content:"• "}
.bullets .cont{padding-left:5px}
.bullets .cont::before{content:""}
.price-table{position:absolute;left:179px;top:338px;width:129px;border-collapse:collapse;background:var(--white);color:var(--ink);font-style:italic;font-size:6.8px}
.price-table td{height:14px;text-align:center;border-bottom:1px solid var(--rule)}
.price-table td:first-child{border-right:1px solid var(--rule);width:66%}
.price-table tr:last-child td{border-bottom:0}
.sheet-footer{position:absolute;left:0;top:408px;width:328px;height:55px;background:var(--teal-band);color:var(--ink)}
.phone{position:absolute;left:20px;top:14px;font-size:11px}
.email{position:absolute;left:20px;top:31px;font-size:8px}
.social{position:absolute;right:20px;top:11px;display:flex;gap:9px}
.social span{width:14px;height:14px;border:1px solid var(--ink);border-radius:50%}
.web{position:absolute;right:20px;top:31px;font-size:8px}
</style>
</head>
<body>

<section class="page cover p1">
  <div class="cover-photo" role="img" aria-label="Bright living room interior with teal tint"></div>
  <div class="cover-logo"><div class="brand-name">brimfield</div><div class="brand-sub">Electrical</div></div>
  <div class="cover-product" role="img" aria-label="White LED downlight product photo"></div>
  <h1 class="cover-title">LED Downlights</h1>
</section>

<section class="page p2">
  <header class="sheet-header"><div class="brand-name">brimfield</div><div class="brand-sub">Electrical</div></header>
  <div class="sheet-photo photo-a" role="img" aria-label="Dim office interior with glass partitions"></div>
  <div class="product-shot" role="img" aria-label="Tiltable LED downlight product photo"></div>
  <h2 class="sheet-title">Parvane Oslira 9w LED</h2><div class="title-rule"></div>
  <div class="sheet-body">
    <p class="intro">Lorem ipsum dolor sit amet, consec<br>tetur adipiscing elit. Sed mattis varius<br>aliquet. Phasellus rhoncus ligula con<br>gue ultrices imperdiet. Phasellus elit nisi,<br>faucibus et laoreet at, dignissim eget nibh.</p>
    <p class="sec-head">Product Features</p>
    <ul class="bullets"><li>Efficient lighting, 9W LED - fully replace</li><li class="cont">35W HAL7W LED MR16 fully replace 50W HAL</li><li>80% energy saving compared with HAL MR16</li><li>Less replacement to save maintenance cost</li><li>Standard IEC size, standard lamp holder, compatible</li><li class="cont">with electronic transformer</li><li>Dimmable</li></ul>
    <p class="sec-head">Technical Specifications</p>
    <ul class="bullets"><li>Average life: 25.000hrs</li><li>Multiple color temperature: 2700K/3000K/4000K</li><li>Color rendering index: 80</li></ul>
    <p class="sec-head">Application</p>
    <ul class="bullets"><li>Hotels, restaurants, cafes, household</li></ul>
    <p class="sec-head">Dimensions</p>
    <ul class="bullets"><li>xxxxxxx</li></ul>
  </div>
  <table class="price-table"><tr><td>1-10 lights</td><td>$49</td></tr><tr><td>11-20 lights</td><td>$45</td></tr><tr><td>21-40 lights</td><td>$42</td></tr><tr><td>41 and over</td><td>$40</td></tr></table>
  <footer class="sheet-footer"><span class="phone">0400 555 019</span><span class="email">info@brimfield.com.au</span><div class="social"><span></span><span></span><span></span></div><span class="web">www.brimfield.com.au</span></footer>
</section>

<section class="page p3">
  <header class="sheet-header"><div class="brand-name">brimfield</div><div class="brand-sub">Electrical</div></header>
  <div class="sheet-photo photo-b" role="img" aria-label="Kitchen with exposed brick wall and pendant lights"></div>
  <div class="product-shot" role="img" aria-label="Recessed LED downlight with spring clips"></div>
  <h2 class="sheet-title">Parvane Oslira 9w LED</h2><div class="title-rule"></div>
  <div class="sheet-body">
    <p class="intro">Lorem ipsum dolor sit amet, consec<br>tetur adipiscing elit. Sed mattis varius<br>aliquet. Phasellus rhoncus ligula con<br>gue ultrices imperdiet. Phasellus elit nisi,<br>faucibus et laoreet at, dignissim eget nibh.</p>
    <p class="sec-head">Product Features</p>
    <ul class="bullets"><li>Efficient lighting, 9W LED - fully replace</li><li class="cont">35W HAL7W LED MR16 fully replace 50W HAL</li><li>80% energy saving compared with HAL MR16</li><li>Less replacement to save maintenance cost</li><li>Standard IEC size, standard lamp holder, compatible</li><li class="cont">with electronic transformer</li><li>Dimmable</li></ul>
    <p class="sec-head">Technical Specifications</p>
    <ul class="bullets"><li>Average life: 25.000hrs</li><li>Multiple color temperature: 2700K/3000K/4000K</li><li>Color rendering index: 80</li></ul>
    <p class="sec-head">Application</p>
    <ul class="bullets"><li>Hotels, restaurants, cafes, household</li></ul>
    <p class="sec-head">Dimensions</p>
    <ul class="bullets"><li>xxxxxxx</li></ul>
  </div>
  <table class="price-table"><tr><td>1-10 lights</td><td>$49</td></tr><tr><td>11-20 lights</td><td>$45</td></tr><tr><td>21-40 lights</td><td>$42</td></tr><tr><td>41 and over</td><td>$40</td></tr></table>
  <footer class="sheet-footer"><span class="phone">0400 555 019</span><span class="email">info@brimfield.com.au</span><div class="social"><span></span><span></span><span></span></div><span class="web">www.brimfield.com.au</span></footer>
</section>

<section class="page p4">
  <header class="sheet-header"><div class="brand-name">brimfield</div><div class="brand-sub">Electrical</div></header>
  <div class="sheet-photo photo-c" role="img" aria-label="Living room with red sofa at night"></div>
  <div class="product-shot" role="img" aria-label="Slim white LED downlight with heat sink"></div>
  <h2 class="sheet-title">Parvane Oslira 9w LED</h2><div class="title-rule"></div>
  <div class="sheet-body">
    <p class="intro">Lorem ipsum dolor sit amet, consec<br>tetur adipiscing elit. Sed mattis varius<br>aliquet. Phasellus rhoncus ligula con<br>gue ultrices imperdiet. Phasellus elit nisi,<br>faucibus et laoreet at, dignissim eget nibh.</p>
    <p class="sec-head">Product Features</p>
    <ul class="bullets"><li>Efficient lighting, 9W LED - fully replace</li><li class="cont">35W HAL7W LED MR16 fully replace 50W HAL</li><li>80% energy saving compared with HAL MR16</li><li>Less replacement to save maintenance cost</li><li>Standard IEC size, standard lamp holder, compatible</li><li class="cont">with electronic transformer</li><li>Dimmable</li></ul>
    <p class="sec-head">Technical Specifications</p>
    <ul class="bullets"><li>Average life: 25.000hrs</li><li>Multiple color temperature: 2700K/3000K/4000K</li><li>Color rendering index: 80</li></ul>
    <p class="sec-head">Application</p>
    <ul class="bullets"><li>Hotels, restaurants, cafes, household</li></ul>
    <p class="sec-head">Dimensions</p>
    <ul class="bullets"><li>xxxxxxx</li></ul>
  </div>
  <table class="price-table"><tr><td>1-10 lights</td><td>$49</td></tr><tr><td>11-20 lights</td><td>$45</td></tr><tr><td>21-40 lights</td><td>$42</td></tr><tr><td>41 and over</td><td>$40</td></tr></table>
  <footer class="sheet-footer"><span class="phone">0400 555 019</span><span class="email">info@brimfield.com.au</span><div class="social"><span></span><span></span><span></span></div><span class="web">www.brimfield.com.au</span></footer>
</section>

<section class="page p5">
  <header class="sheet-header"><div class="brand-name">brimfield</div><div class="brand-sub">Electrical</div></header>
  <div class="sheet-photo photo-d" role="img" aria-label="Office interior with window blinds"></div>
  <div class="product-shot" role="img" aria-label="Flat panel LED downlight"></div>
  <h2 class="sheet-title">Parvane Oslira 9w LED</h2><div class="title-rule"></div>
  <div class="sheet-body">
    <p class="intro">Lorem ipsum dolor sit amet, consec<br>tetur adipiscing elit. Sed mattis varius<br>aliquet. Phasellus rhoncus ligula con<br>gue ultrices imperdiet. Phasellus elit nisi,<br>faucibus et laoreet at, dignissim eget nibh.</p>
    <p class="sec-head">Product Features</p>
    <ul class="bullets"><li>Efficient lighting, 9W LED - fully replace</li><li class="cont">35W HAL7W LED MR16 fully replace 50W HAL</li><li>80% energy saving compared with HAL MR16</li><li>Less replacement to save maintenance cost</li><li>Standard IEC size, standard lamp holder, compatible</li><li class="cont">with electronic transformer</li><li>Dimmable</li></ul>
    <p class="sec-head">Technical Specifications</p>
    <ul class="bullets"><li>Average life: 25.000hrs</li><li>Multiple color temperature: 2700K/3000K/4000K</li><li>Color rendering index: 80</li></ul>
    <p class="sec-head">Application</p>
    <ul class="bullets"><li>Hotels, restaurants, cafes, household</li></ul>
    <p class="sec-head">Dimensions</p>
    <ul class="bullets"><li>xxxxxxx</li></ul>
  </div>
  <table class="price-table"><tr><td>1-10 lights</td><td>$49</td></tr><tr><td>11-20 lights</td><td>$45</td></tr><tr><td>21-40 lights</td><td>$42</td></tr><tr><td>41 and over</td><td>$40</td></tr></table>
  <footer class="sheet-footer"><span class="phone">0400 555 019</span><span class="email">info@brimfield.com.au</span><div class="social"><span></span><span></span><span></span></div><span class="web">www.brimfield.com.au</span></footer>
</section>

<section class="page p6">
  <header class="sheet-header"><div class="brand-name">brimfield</div><div class="brand-sub">Electrical</div></header>
  <div class="sheet-photo photo-e" role="img" aria-label="Lounge room with pendant lamp"></div>
  <div class="product-shot" role="img" aria-label="Deep recessed LED downlight with heat sink"></div>
  <h2 class="sheet-title">Parvane Oslira 9w LED</h2><div class="title-rule"></div>
  <div class="sheet-body">
    <p class="intro">Lorem ipsum dolor sit amet, consec<br>tetur adipiscing elit. Sed mattis varius<br>aliquet. Phasellus rhoncus ligula con<br>gue ultrices imperdiet. Phasellus elit nisi,<br>faucibus et laoreet at, dignissim eget nibh.</p>
    <p class="sec-head">Product Features</p>
    <ul class="bullets"><li>Efficient lighting, 9W LED - fully replace</li><li class="cont">35W HAL7W LED MR16 fully replace 50W HAL</li><li>80% energy saving compared with HAL MR16</li><li>Less replacement to save maintenance cost</li><li>Standard IEC size, standard lamp holder, compatible</li><li class="cont">with electronic transformer</li><li>Dimmable</li></ul>
    <p class="sec-head">Technical Specifications</p>
    <ul class="bullets"><li>Average life: 25.000hrs</li><li>Multiple color temperature: 2700K/3000K/4000K</li><li>Color rendering index: 80</li></ul>
    <p class="sec-head">Application</p>
    <ul class="bullets"><li>Hotels, restaurants, cafes, household</li></ul>
    <p class="sec-head">Dimensions</p>
    <ul class="bullets"><li>xxxxxxx</li></ul>
  </div>
  <table class="price-table"><tr><td>1-10 lights</td><td>$49</td></tr><tr><td>11-20 lights</td><td>$45</td></tr><tr><td>21-40 lights</td><td>$42</td></tr><tr><td>41 and over</td><td>$40</td></tr></table>
  <footer class="sheet-footer"><span class="phone">0400 555 019</span><span class="email">info@brimfield.com.au</span><div class="social"><span></span><span></span><span></span></div><span class="web">www.brimfield.com.au</span></footer>
</section>

</body>
</html>
```